Awesome Business Card Design needed!

Hey there.
I'm looking for a simple but awesome business card design.
Type of company: Online advertisement agency
(please don't use the typical business people or statistics images on the card)
The front has to display the business name
and possibly some sort of logo ( perhaps something with the two M's of the biz name )
And the back of the card should say:
Name
Phone
Email
Let your imagination flow.
here are some designs that I like and that you can use as inspiration.
Simple but Awesome
http://images.pixelvantor.net/designs/55128_877673_43091_thumbnail.jpg
http://images.pixelvantor.net/designs/37714_747642_40106_image.jpg
http://images.pixelvantor.net/designs/55128_877673_43091_image.jpg
http://images.pixelvantor.net/designs/51321_781878_43091_image.jpg
http://images.pixelvantor.net/designs/33378_399063_15912_image.jpg
http://images.pixelvantor.net/designs/2337_271604_9495_image.jpg
good luck

```html
<!DOCTYPE html>
<html lang="en">
<head>
<meta charset="utf-8">
<title>Varnelo Media – Business Card</title>
<link rel="stylesheet" href="https://fonts.googleapis.com/css2?family=Arimo&family=Comfortaa:wght@300;700&display=swap">
<style>
  :root {
    --paper: #ffffff;
    --frame: #000000;
    --ink: #000000;
    --card-dark: #000000;
    --card-light: #dedede;
    --shadow: #9a9a9a;
    --contact-ink: #1e1e1e;
    --divider: #4a4a4a;
  }
  html, body {
    margin: 0;
    padding: 0;
    overflow: hidden;
    background: var(--paper);
  }
  .sheet {
    position: relative;
    width: 1200px;
    height: 872px;
    overflow: hidden;
    background: var(--paper);
  }
  .sheet-frame {
    position: absolute;
    left: 0;
    top: 0;
    width: 1160px;
    height: 869px;
    border: 1.5px solid var(--frame);
    box-sizing: border-box;
    z-index: 2;
    pointer-events: none;
  }
  .side-label {
    position: absolute;
    margin: 0;
    font-family: "Arimo", Arial, sans-serif;
    font-weight: 400;
    font-size: 94px;
    line-height: 1;
    color: var(--ink);
  }
  .side-label--front { left: 36px; top: 180px; }
  .side-label--back { left: 609px; top: 158px; }
  .card-shadow {
    position: absolute;
    background: var(--shadow);
    filter: blur(9px);
  }
  .card-shadow--front { left: 32px; top: 365px; width: 536px; height: 295px; }
  .card-shadow--back { left: 622px; top: 365px; width: 514px; height: 295px; }
  .card {
    position: absolute;
    overflow: hidden;
  }
  .card--front { left: 34px; top: 266px; width: 551px; height: 276px; }
  .card--back { left: 588px; top: 264px; width: 550px; height: 278px; }
  .card svg { display: block; }
  .brand-name {
    font-family: "Comfortaa", sans-serif;
    font-weight: 700;
    fill: var(--ink);
  }
  .contact-line {
    font-family: "Comfortaa", sans-serif;
    font-weight: 300;
    font-size: 15px;
    fill: var(--contact-ink);
  }
</style>
</head>
<body>
<main class="sheet">
  <div class="sheet-frame"></div>

  <h2 class="side-label side-label--front">Front side</h2>
  <h2 class="side-label side-label--back">Back side</h2>

  <div class="card-shadow card-shadow--front"></div>
  <div class="card-shadow card-shadow--back"></div>

  <section class="card card--front" aria-label="Card front">
    <svg width="551" height="276" viewBox="0 0 551 276">
      <defs>
        <linearGradient id="front-fade" x1="0" y1="0" x2="1" y2="0">
          <stop offset="0" stop-color="var(--card-dark)"/>
          <stop offset="1" stop-color="var(--card-light)"/>
        </linearGradient>
        <radialGradient id="lens-tone" cx="0.5" cy="0.5" r="0.5">
          <stop offset="0" stop-color="#6a6a6a"/>
          <stop offset="0.55" stop-color="#1a1a1a"/>
          <stop offset="0.85" stop-color="#bdbdbd"/>
          <stop offset="1" stop-color="#5a5a5a"/>
        </radialGradient>
      </defs>
      <rect class="card-base" width="551" height="276" fill="url(#front-fade)"/>
      <rect class="card-band" x="0" y="121" width="551" height="39" fill="#ffffff" opacity="0.1"/>
      <path class="card-sweep" d="M10 276 Q200 160 551 125" fill="none" stroke="#ffffff" stroke-opacity="0.18" stroke-width="1.5"/>
      <text class="brand-name" x="212" y="160" font-size="25">Varnelo Media</text>
      <circle class="lens-art" role="img" aria-label="Camera lens illustration" cx="496" cy="136" r="54" fill="url(#lens-tone)"/>
    </svg>
  </section>

  <section class="card card--back" aria-label="Card back">
    <svg width="550" height="278" viewBox="0 0 550 278">
      <defs>
        <linearGradient id="back-fade" x1="0" y1="0" x2="1" y2="0">
          <stop offset="0" stop-color="var(--card-dark)"/>
          <stop offset="1" stop-color="var(--card-light)"/>
        </linearGradient>
        <linearGradient id="band-fade" x1="0" y1="0" x2="1" y2="0">
          <stop offset="0" stop-color="#ffffff" stop-opacity="0.05"/>
          <stop offset="1" stop-color="#ffffff" stop-opacity="0.45"/>
        </linearGradient>
      </defs>
      <rect class="card-base" width="550" height="278" fill="url(#back-fade)"/>
      <rect class="card-band" x="0" y="121" width="550" height="62" fill="url(#band-fade)"/>
      <path class="card-sweep" d="M10 278 Q180 170 320 162" fill="none" stroke="#ffffff" stroke-opacity="0.18" stroke-width="1.5"/>
      <text class="contact-line" x="60" y="139">Name</text>
      <text class="contact-line" x="60" y="158">Phone</text>
      <text class="contact-line" x="60" y="177">Email</text>
      <line class="card-divider" x1="336" y1="92" x2="336" y2="202" stroke="var(--divider)" stroke-width="3"/>
      <text class="brand-name" x="346" y="158" font-size="15">Varnelo Media</text>
    </svg>
  </section>
</main>
</body>
</html>
```